Stationery Design Project

We need a stationary design for a well-known architect in Guadalajara, Mexico. This architect specializes in very luxurious homes and commercial developments. His clients are very sophisticated, so the letterhead should be equally sophisticated. References to mythology, etc. might be a plus. The letterhead may be embossed and will be printed on a heavy-weight linen. His homes and developments are very luxurious but not necessarily ultra-modern in their aesthetic.
Target Market(s)
High end developers and luxury home buyers
Industry/Entity Type
Architect
Look and feel

```html
<!DOCTYPE html>
<html lang="en">
<head>
<meta charset="utf-8">
<title>Dario Valero – Stationery</title>
<link rel="stylesheet" href="https://fonts.googleapis.com/css2?family=Jost:wght@300;400&display=swap">
<style>
  :root {
    --brown: #5b3a10;
    --orange: #f39c00;
    --yellow: #fcc500;
    --tel: #c98a1c;
    --paper: #ffffff;
    --edge: #222222;
    --card-edge: #d8d0c0;
  }
  * { margin: 0; padding: 0; box-sizing: border-box; }
  html, body { width: 1200px; height: 842px; overflow: hidden; background: var(--paper); }
  body { position: relative; font-family: "Jost", "Futura", sans-serif; color: var(--brown); }

  .brand-name {
    position: absolute;
    font-weight: 400;
    color: var(--brown);
    white-space: nowrap;
    line-height: 1;
    letter-spacing: 1px;
  }
  .brand-name--header { left: 97px; top: 124px; font-size: 24px; }

  .sheet { position: absolute; background: var(--paper); }
  .letterhead { left: 646px; top: 104px; width: 458px; height: 643px; border: 2px solid var(--edge); }
  .envelope { left: 356px; top: 499px; width: 557px; height: 253px; border: 1px solid var(--edge); z-index: 2; }

  .card { position: absolute; top: 107px; width: 121px; height: 248px; border: 1px solid var(--card-edge); }
  .card--front { left: 331px; background: var(--orange); }
  .card--back { left: 456px; background: var(--yellow); }

  .card--front .brand-name { left: 12px; top: 200px; font-size: 13px; }
  .role { position: absolute; left: 78px; top: 229px; font-size: 8px; font-weight: 300; }

  .color-band { position: absolute; top: 0; width: 67px; height: 138px; background: var(--orange); }

  .contact { position: absolute; font-size: 9px; font-weight: 300; line-height: 12.5px; }
  .contact__tel { color: var(--tel); }
  .card--back .contact { right: 4px; top: 172px; text-align: right; line-height: 11.5px; }
  .card--back .contact__tel { margin-top: 2px; display: block; }

  .sheet .brand-name { font-size: 15px; top: 22px; }
</style>
</head>
<body>

  <p class="brand-name brand-name--header">DARIO VALERO</p>

  <div class="card card--front">
    <p class="brand-name">DARIO VALERO</p>
    <span class="role">Architect</span>
  </div>

  <div class="card card--back">
    <p class="contact">
      Calle de los Arcos #1450<br>
      Colinas del Rio<br>
      Tlaquepaque, Jalisco 45580<br>
      Mexico<br>
      <span class="contact__tel">Tel (52) 33 55 01 48 72</span>
    </p>
  </div>

  <div class="sheet letterhead">
    <div class="color-band" style="left:22px;"></div>
    <p class="brand-name" style="left:96px;">DARIO VALERO</p>
    <p class="contact" style="left:94px; top:90px;">
      Calle de los Arcos #1450,<br>
      Colinas del Rio, Tlaquepaque,<br>
      Jalisco 45580, Mexico<br>
      <span class="contact__tel">Tel (52) 33 55 01 48 72</span>
    </p>
  </div>

  <div class="sheet envelope">
    <div class="color-band" style="left:14px;"></div>
    <p class="brand-name" style="left:88px;">DARIO VALERO</p>
    <p class="contact" style="left:86px; top:90px;">
      Calle de los Arcos #1450,<br>
      Colinas del Rio, Tlaquepaque,<br>
      Jalisco 45580, Mexico<br>
      <span class="contact__tel">Tel (52) 33 55 01 48 72</span>
    </p>
  </div>

</body>
</html>
```